Flyer
Zielgruppe
Wir sind eine Versicherungsmaklerfirma und benötigen einen Flyer zur Vorstellung unserer Firma bei Privatkunden und Selbstständigen.
Aufgabenstellung
Es kann das Design der Homepage aufgegriffen werden oder eigene Designvorschläge gemacht werden.
Für den Text (Inhalt) legen wir eine Word Datei bei bzw. können Informationen unserer Homepage herangezogen werden. Als Format wäre ein Falzflyer oder Din A5 gefaltet (4 Seiten) gut. Es soll Interesse für eine Beratung geweckt werden. Wenn möglich sollten 2 Beispielkunden (Musterkunde 1 Familie mit 4 Versicherungen) (Musterkunde 2 Selbstständig mit einem Firmen KFZ) eingebaut werden als Bild oder mit einem kurzen Text. und hier insbesondere eine Einsparung nach einer Beratung/Versicherungsvergleich aufgezeigt werden. Sofern genügend Platz auf dem Flyer kann auch das Maklerteam vorgestellt werden.

```html
<!DOCTYPE html>
<html lang="de">
<head>
<meta charset="utf-8">
<title>VANTO Assekuranzmakler – Flyer</title>
<link href="https://fonts.googleapis.com/css2?family=Poppins:ital,wght@0,400;0,500;0,600;0,700;0,800;1,400&display=swap" rel="stylesheet">
<style>
:root{
  --navy:#1d2a6b;
  --navy-deep:#141d4f;
  --orange:#ef7a24;
  --paper:#ffffff;
  --ink:#2b2b33;
  --stage:#a3a4a7;
}
*{margin:0;padding:0;box-sizing:border-box}
html,body{width:803px;height:1200px;overflow:hidden;background:var(--stage);font-family:"Poppins",sans-serif;color:var(--ink)}
.spread{position:absolute;left:20px;width:763px;height:540px;background:var(--paper);box-shadow:0 3px 10px rgba(0,0,0,.25);overflow:hidden}
.spread--outer{top:40px}
.spread--inner{top:620px;background:linear-gradient(90deg,#ececef 0%,#fafafa 50%,#f1f1f3 100%)}
.spread svg.backdrop{position:absolute;inset:0}
.abs{position:absolute}
.brand{position:absolute;text-align:center;color:var(--navy);font-weight:800;line-height:1}
.brand__name{display:block;letter-spacing:1px}
.brand__line{display:block;font-weight:400;letter-spacing:.3px}
.brand--cover{left:100px;top:268px;width:200px}
.brand--cover .brand__name{font-size:52px}
.brand--cover .brand__line{font-size:13px;margin-top:2px}
.brand--photo{left:590px;top:28px;width:160px;color:#fff}
.brand--photo .brand__name{font-size:40px}
.brand--photo .brand__line{font-size:11px;margin-top:2px;color:#e6e8f0}
.brand--closing{left:555px;top:408px;width:170px}
.brand--closing .brand__name{font-size:46px}
.brand--closing .brand__line{font-size:11px;margin-top:2px}
.contact{left:50px;top:398px;color:#fff}
.contact__title{font-size:13px;font-weight:600}
.contact__rule{width:120px;height:1.5px;background:#fff;margin:2px 0 8px}
.contact__item{display:flex;align-items:center;gap:7px;font-size:10.5px;font-weight:500;margin-bottom:5px}
.contact__item:first-of-type{font-size:12px;font-weight:700}
.contact__icon{width:11px;height:11px;border-radius:50%;background:var(--orange);display:inline-flex;align-items:center;justify-content:center;flex:none}
.welcome{left:400px;top:298px;width:345px;text-align:center}
.welcome h1{font-size:14.5px;font-weight:700;color:var(--navy);line-height:1.2}
.welcome h1 em{font-style:normal;color:var(--orange)}
.welcome .sub{font-size:8.5px;font-style:italic;margin-top:3px;line-height:1.25}
.pill{display:inline-block;margin:9px 0 8px;background:var(--orange);color:#fff;font-size:10.5px;font-weight:700;padding:3px 16px;border-radius:11px}
.welcome p.body{font-size:7.6px;line-height:1.4}
.welcome .advantage{font-size:9px;font-weight:700;color:var(--navy);margin-top:14px}
h2.section{font-size:10.5px;font-weight:700;color:var(--navy);line-height:1.25}
.rule{width:95px;height:2px;background:var(--orange);margin:4px 0 8px}
.list{list-style:none}
.list li{display:flex;gap:6px;margin-bottom:7px}
.list svg{flex:none;margin-top:1px}
.list li > div{font-size:7.2px;line-height:1.3}
.list strong{display:block;font-size:8px;font-weight:700;color:var(--navy-deep);line-height:1.25}
.list span{display:block;font-size:7.2px;line-height:1.3}
.intro{left:30px;top:22px;width:300px;font-size:9px;line-height:1.25}
.intro b{font-weight:700;color:var(--navy-deep)}
.benefits{left:32px;top:58px;width:320px}
.story{left:30px;top:150px;width:350px;color:#fff}
.story h3{font-size:10.5px;font-weight:700;margin-bottom:4px}
.story p{font-size:7.2px;line-height:1.35}
.why{left:30px;top:342px;width:340px}
.why .list li{margin-bottom:9px}
.services{left:398px;top:16px;width:343px;height:294px;border:1.5px solid var(--orange);padding:18px 16px 0}
.services .rule{background:var(--navy);width:80px}
.services .list li{margin-bottom:8px}
.services ul.sub{list-style:none;margin-top:2px}
.services ul.sub li{display:block;margin:0;font-size:7px;line-height:1.35;padding-left:9px;position:relative}
.services ul.sub li::before{content:"";position:absolute;left:1px;top:4px;width:3px;height:3px;border-radius:50%;background:var(--orange)}
.services ul.sub b{font-weight:700}
.cta{left:400px;top:322px;width:345px}
.cta h2{font-size:11.5px;font-weight:700;color:var(--navy)}
.cta p{font-size:7.2px;line-height:1.4;margin-top:12px}
.cta p b{font-weight:700}
.appointment{left:410px;top:404px;width:150px}
.appointment .big{font-size:13px;font-weight:700;color:var(--navy);line-height:1.15}
.appointment .big em{font-style:normal;color:var(--orange)}
.appointment .small{font-size:7px;color:var(--navy);margin-top:3px;line-height:1.3}
</style>
</head>
<body>
<svg width="0" height="0" style="position:absolute">
  <defs>
    <symbol id="tick" viewBox="0 0 12 12"><circle cx="6" cy="6" r="6" fill="currentColor"/><path d="M3.3 6.2l1.8 1.8 3.6-3.8" fill="none" stroke="#fff" stroke-width="1.5" stroke-linecap="round" stroke-linejoin="round"/></symbol>
    <linearGradient id="navyBand" x1="0" y1="0" x2="1" y2="1"><stop offset="0" stop-color="#24327a"/><stop offset="1" stop-color="#141d4f"/></linearGradient>
    <linearGradient id="skyPhoto" x1="0" y1="0" x2="0" y2="1"><stop offset="0" stop-color="#b9c6d6"/><stop offset=".6" stop-color="#5f7594"/><stop offset="1" stop-color="#9aa2ac"/></linearGradient>
    <linearGradient id="officePhoto" x1="0" y1="0" x2="1" y2="1"><stop offset="0" stop-color="#1c2244"/><stop offset=".55" stop-color="#3a3f5c"/><stop offset="1" stop-color="#cfcfd4"/></linearGradient>
    <linearGradient id="warmPhoto" x1="0" y1="0" x2="1" y2="1"><stop offset="0" stop-color="#c9a27c"/><stop offset="1" stop-color="#6d5444"/></linearGradient>
    <linearGradient id="carPhoto" x1="0" y1="0" x2="1" y2="1"><stop offset="0" stop-color="#aab4c2"/><stop offset="1" stop-color="#dadde2"/></linearGradient>
    <linearGradient id="familyPhoto" x1="0" y1="0" x2="1" y2="1"><stop offset="0" stop-color="#f1ece6"/><stop offset="1" stop-color="#c9b39c"/></linearGradient>
    <linearGradient id="driverPhoto" x1="0" y1="0" x2="1" y2="1"><stop offset="0" stop-color="#3c3f48"/><stop offset="1" stop-color="#b7bcc4"/></linearGradient>
  </defs>
</svg>

<section class="spread spread--outer">
  <svg class="backdrop" width="763" height="540" viewBox="0 0 763 540">
    <polygon points="0,0 382,0 382,205 0,108" fill="url(#skyPhoto)" role="img" aria-label="Foto: modernes Bürogebäude unter Himmel"/>
    <polygon points="382,0 763,0 763,205 570,276 382,214" fill="url(#officePhoto)" role="img" aria-label="Foto: Makler im Beratungsgespräch am Schreibtisch"/>
    <polygon points="645,243 763,198 763,268" fill="var(--orange)"/>
    <rect x="36" y="126" width="128" height="112" fill="url(#warmPhoto)" stroke="#fff" stroke-width="3" role="img" aria-label="Foto: Paar prüft Unterlagen zu Hause"/>
    <rect x="170" y="122" width="135" height="118" fill="url(#carPhoto)" stroke="#fff" stroke-width="3" role="img" aria-label="Foto: Mann neben seinem Auto"/>
    <path d="M0,368 C150,400 300,440 560,540 L0,540 Z" fill="url(#navyBand)"/>
  </svg>

  <div class="brand brand--cover"><span class="brand__name">VANTO</span><span class="brand__line">Assekuranzmakler</span></div>

  <div class="abs contact">
    <div class="contact__title">Kontakt</div>
    <div class="contact__rule"></div>
    <div class="contact__item"><span class="contact__icon"><svg width="7" height="7" viewBox="0 0 10 10"><path d="M2 1l2 2-1 1.3c.6 1.3 1.4 2.1 2.7 2.7L7 6l2 2-1.2 1.5C4.5 9 1 5.5.5 2.2Z" fill="#fff"/></svg></span>+49 911 4820175</div>
    <div class="contact__item"><span class="contact__icon"><svg width="7" height="7" viewBox="0 0 10 10"><rect x="1" y="2.5" width="8" height="5.5" fill="none" stroke="#fff" stroke-width="1.2"/><path d="M1 2.5l4 3 4-3" fill="none" stroke="#fff" stroke-width="1.2"/></svg></span>makler.hollrath@postfeld.org</div>
    <div class="contact__item"><span class="contact__icon"><svg width="7" height="7" viewBox="0 0 10 10"><circle cx="5" cy="5" r="3.8" fill="none" stroke="#fff" stroke-width="1.1"/><path d="M1.2 5h7.6M5 1.2c-2 2.4-2 5.2 0 7.6M5 1.2c2 2.4 2 5.2 0 7.6" fill="none" stroke="#fff" stroke-width=".9"/></svg></span>www.vanto-assekuranz.de</div>
  </div>

  <div class="brand brand--photo"><span class="brand__name">VANTO</span><span class="brand__line">Assekuranzmakler</span></div>

  <div class="abs welcome">
    <h1>Herzlich Willkommen bei <em>VANTO</em><br>Assekuranz Versicherungsmakler!</h1>
    <div class="sub">Ihr vertrauensvoller Partner für Versicherungen in<br>Nürnberg &amp; Mittelfranken</div>
    <div class="pill">Persönlich. Transparent. Unabhängig.</div>
    <p class="body">Haben Sie schon einmal Ihre Versicherungsbedingungen genau durchgelesen? Wissen Sie wirklich, welche Leistungen im Schadensfall greifen – oder auch nicht? Wir helfen Ihnen dabei, Ihre Absicherung zu optimieren, unnötige Kosten zu vermeiden und gleichzeitig Ihre finanzielle Sicherheit zu stärken.</p>
    <div class="advantage">hr Vorteil: Clever vergleichen &amp; sparen!</div>
  </div>
</section>

<section class="spread spread--inner">
  <svg class="backdrop" width="763" height="540" viewBox="0 0 763 540">
    <rect x="0" y="140" width="398" height="152" fill="var(--orange)"/>
    <rect x="35" y="246" width="150" height="86" fill="url(#familyPhoto)" stroke="#fff" stroke-width="3" role="img" aria-label="Foto: Familie im Beratungsgespräch"/>
    <rect x="190" y="242" width="155" height="88" fill="url(#driverPhoto)" stroke="#fff" stroke-width="3" role="img" aria-label="Foto: Frau am Steuer ihres Firmenwagens"/>
    <polygon points="630,540 763,488 763,540" fill="url(#navyBand)"/>
  </svg>

  <div class="abs intro">Mit VANTO Versicherungsmakler haben Sie<br><b>zwei entscheidende Vorteile kombiniert:</b></div>

  <ul class="abs list benefits">
    <li><svg width="10" height="10" style="color:var(--orange)"><use href="#tick"/></svg><div><strong>Günstige und leistungsstarke Produkte –</strong><span>Dank unseres unabhängigen Versicherungsvergleichs.</span></div></li>
    <li><svg width="10" height="10" style="color:var(--orange)"><use href="#tick"/></svg><div><strong>Persönliche Betreuung –</strong><span>Wir stehen Ihnen jederzeit beratend zur Seite, insbesondere<br>im Schadensfall.</span></div></li>
  </ul>

  <div class="abs story">
    <h3>Unsere Erfolgsgeschichten – Ihre Ersparnis!</h3>
    <p><b>Familie Berger</b> – Die klassische Familie mit 4-5 Versicherungen (z. B. Hausrat, Haftpflicht, Kfz, Unfall, Rechtsschutz) konnte durch unseren Service <b>730€ pro Jahr</b> einsparen! Firmenkunde – Ein Unternehmer optimierte mit unserer Hilfe seine KFZ Versicherung des Firmenwagens und senkte die Kosten für seinen Firmenwagen um <b>660€ jährlich.</b></p>
  </div>

  <div class="abs why">
    <h2 class="section">Warum VANTO Versicherungsmakler?</h2>
    <div class="rule"></div>
    <ul class="list">
      <li><svg width="10" height="10" style="color:var(--navy)"><use href="#tick"/></svg><div><strong>Unabhängig &amp; fair:</strong><span>Wir sind keine Vertreter einer bestimmten Versicherung – wirarbeiten für SIE!</span></div></li>
      <li><svg width="10" height="10" style="color:var(--navy)"><use href="#tick"/></svg><div><strong>Maßgeschneiderte Lösungen:</strong><span>Jeder Kunde hat individuelle Bedürfnisse – wir finden dieoptimale Absicherung.</span></div></li>
      <li><svg width="10" height="10" style="color:var(--navy)"><use href="#tick"/></svg><div><strong>Transparente Beratung:</strong><span>Verständlich, ehrlich und ohne versteckte Klauseln.</span></div></li>
      <li><svg width="10" height="10" style="color:var(--navy)"><use href="#tick"/></svg><div><strong>100% kostenfrei:</strong><span>Unsere Beratung kostet Sie nichts – Sie profitieren einfach von besserenTarifen.</span></div></li>
    </ul>
  </div>

  <div class="abs services">
    <h2 class="section">Unsere Dienstleistungen im Überblick:</h2>
    <div class="rule"></div>
    <ul class="list">
      <li><svg width="10" height="10" style="color:var(--navy)"><use href="#tick"/></svg><div><strong>Versicherungs-TÜV – Wir checken Ihre bestehenden Verträge</strong>
        <ul class="sub"><li>Passt Ihr Versicherungsschutz wirklich zu Ihrer Lebenssituation?</li><li>Sind Sie möglicherweise überversichert oder zahlen zu viel?</li><li>Wir überprüfen Ihre Policen und zeigen Ihnen Einsparpotenziale auf!</li></ul></div></li>
      <li><svg width="10" height="10" style="color:var(--navy)"><use href="#tick"/></svg><div><strong>Persönliche Beratung – Verständlich &amp; unabhängig</strong>
        <ul class="sub"><li>Sie erhalten eine ehrliche, faire und für <b>Sie nachvollziehbare Beratung.</b></li><li>Kein Fachchinesisch – wir erklären Ihnen genau, welche Leistungen für Sie sinnvoll sind. Wir zeigen Ihnen, wie Sie <b>direkt beim Versicherer „ ab Werk“ einkaufen</b> – ohne teureZwischenstationen.</li></ul></div></li>
      <li><svg width="10" height="10" style="color:var(--navy)"><use href="#tick"/></svg><div><strong>Betreuungskonzepte – Ganz nach Ihrem Bedarf</strong>
        <ul class="sub"><li>Ob Sie eine intensive Betreuung oder nur gelegentliche Check-ups wünschen – wir haben das passende Konzept für Sie.</li></ul></div></li>
      <li><svg width="10" height="10" style="color:var(--navy)"><use href="#tick"/></svg><div><strong>Unser Versprechen: Kein Kleingedrucktes,<br>keine versteckten Kosten</strong>
        <ul class="sub"><li>Keine zusätzlichen Gebühren – <b>unsere Beratung ist für Sie kostenfrei!</b></li><li>Klare, verständliche Vertragsdetails ohne unangenehme Überraschungen.</li></ul></div></li>
    </ul>
  </div>

  <div class="abs cta">
    <h2>Jetzt beraten lassen &amp; profitieren!</h2>
    <p>Seit über 15 Jahren helfen wir Menschen in <b>Nürnberg &amp; in ganz Mittelfranken</b> dabei, ihre Versicherungen zu optimieren – insbesondere in den Bereichen <b>Krankenversicherung,</b> Berufsunfähigkeit &amp; Altersvorsorge. Lassen Sie uns gemeinsam herausfinden, wie Sie <b>mehr Leistung für weniger Geld</b> erhalten!</p>
  </div>

  <div class="abs appointment">
    <div class="big">etzt Termin<br>vereinbaren und<br><em>clever sparen!</em></div>
    <div class="small">VANTO Versicherungsmakler –<br>Ihr Partner für kluge<br>Versicherungsentscheidungen.</div>
  </div>

  <div class="brand brand--closing"><span class="brand__name">VANTO</span><span class="brand__line">Assekuranzmakler</span></div>
</section>
</body>
</html>
```